Bref créative
Brochure design
vantor crew staffing
oil & gas recruitment experts
This company profile will be used to give an introduction about the services and company strategy. Another main objective is to be used for marketing purposes for the company to clients and job seekers in oil and gas
Consulting
Corporate professional looking profile that will provide an introduction for marketing purposes in order to provide new business in the futures
A3 sized page folded once to form an A4 sized brochuer. The conetnt will be on the inside of the brochure. Full colour ideally on white pages
Ai file for Logo (Please use RED & BLUE VERSION)
Please find attached the wording for the brochure
Please use this image on the front page of the Brochure
Please use this or similar image in the brochure
Please use this image or similar image of an African engineer
If you have sufficient space on the page please use t he following imgae of something similar
If you have sufficient space on the brochure please use the attached image or something similar

```html
<!DOCTYPE html>
<html lang="en">
<head>
<meta charset="utf-8">
<title>vantor crew staffing – company profile brochure</title>
<link href="https://fonts.googleapis.com/css2?family=Open+Sans:wght@400;600;700;800&display=swap" rel="stylesheet">
<style>
  :root {
    --bg: #e9ecef;
    --paper: #ffffff;
    --blue-deep: #0b3d78;
    --blue: #1565b0;
    --blue-light: #3d9ad8;
    --red: #d7262e;
    --ink: #2b2f36;
    --ink-soft: #5b6470;
    --photo-warm: #9a8c7a;
    --photo-cool: #6f8fa8;
  }
  * { box-sizing: border-box; margin: 0; padding: 0; }
  html, body { width: 1200px; height: 792px; overflow: hidden; }
  body {
    background: var(--bg);
    font-family: "Open Sans", Arial, sans-serif;
    color: var(--ink);
    position: relative;
  }
  .spread { position: absolute; top: 191px; height: 410px; display: flex; box-shadow: 0 6px 18px rgba(0,0,0,.18); }
  .spread--outside { left: 20px; width: 580px; }
  .spread--inside { left: 620px; width: 560px; }
  .page { position: relative; width: 290px; height: 410px; background: var(--paper); overflow: hidden; }
  .spread--inside .page { width: 280px; }
  .wave { position: absolute; left: 0; top: 0; width: 100%; height: 100%; }

  /* front cover */
  .brand { position: absolute; display: flex; align-items: center; gap: 6px; }
  .brand__mark { width: 12px; height: 12px; background: var(--red); }
  .brand__name { font-weight: 800; font-size: 15px; color: var(--blue-deep); text-transform: lowercase; letter-spacing: .2px; }
  .cover-front .brand { left: 22px; top: 34px; }
  .cover-front__photo {
    position: absolute; left: 120px; top: 82px; width: 170px; height: 150px;
    background: linear-gradient(135deg, var(--photo-cool), #3e5b78 55%, var(--photo-warm));
  }

  /* back cover */
  .cover-back__photo {
    position: absolute; left: 0; top: 128px; width: 160px; height: 128px;
    background: linear-gradient(135deg, #c9c2b6, var(--photo-warm) 60%, #5a4e44);
  }
  .contact { position: absolute; left: 18px; bottom: 24px; width: 170px; }
  .contact__title { background: var(--blue); color: #fff; font-weight: 700; font-size: 7px; padding: 3px 6px; text-transform: lowercase; margin-bottom: 6px; }
  .contact__row { display: flex; align-items: center; gap: 5px; font-size: 6.5px; color: var(--ink); margin-bottom: 4px; }
  .contact__row svg { width: 8px; height: 8px; flex: none; }

  /* inside pages */
  .inside-left__bar { position: absolute; left: 0; top: 0; width: 100%; height: 8px; background: var(--blue); }
  .section-head { display: flex; align-items: center; gap: 5px; font-weight: 700; font-size: 8.5px; color: var(--blue-deep); }
  .section-head__num { width: 13px; height: 13px; border-radius: 50%; background: var(--blue); color: #fff; font-size: 7px; display: flex; align-items: center; justify-content: center; }
  .inside-left__body { position: absolute; left: 18px; top: 20px; right: 18px; }
  .copy { font-size: 5.6px; line-height: 1.55; color: var(--ink-soft); margin-top: 6px; }
  .sub-head { font-weight: 700; font-size: 6.5px; color: var(--blue-deep); margin-top: 8px; }
  .value-list { list-style: none; margin-top: 3px; }
  .value-list li { font-size: 5.6px; line-height: 1.6; color: var(--ink-soft); padding-left: 7px; position: relative; }
  .value-list li::before { content: ""; position: absolute; left: 0; top: 2.5px; width: 3px; height: 3px; background: var(--blue); }
  .services-band {
    position: absolute; left: 0; bottom: 0; width: 100%; height: 118px;
    background: linear-gradient(180deg, var(--blue) 0%, var(--blue-deep) 100%);
    padding: 12px 18px; color: #fff;
  }
  .services-band__title { background: var(--paper); color: var(--blue-deep); font-weight: 700; font-size: 7px; padding: 2px 6px; display: inline-block; text-transform: uppercase; }
  .services-band .copy { color: #dbe8f6; }

  .inside-right__body { position: absolute; left: 18px; top: 22px; right: 18px; }
  .inside-right__title { font-weight: 700; font-size: 9px; color: var(--blue-deep); padding-bottom: 4px; border-bottom: 1px solid var(--blue-light); }
  .service { margin-top: 9px; }
  .service__name { font-weight: 700; font-size: 6.5px; color: var(--blue); }
</style>
</head>
<body>

  <!-- outside: back cover + front cover -->
  <section class="spread spread--outside">
    <article class="page cover-back">
      <svg class="wave" viewBox="0 0 290 410" preserveAspectRatio="none" aria-hidden="true">
        <defs>
          <linearGradient id="backWave" x1="0" y1="0" x2="1" y2="1">
            <stop offset="0" stop-color="#3d9ad8"/>
            <stop offset="1" stop-color="#0b3d78"/>
          </linearGradient>
        </defs>
        <path d="M150 0 H290 V300 C250 250 210 170 150 0 Z" fill="url(#backWave)"/>
        <path d="M185 0 C215 120 250 210 290 260" stroke="#fff" stroke-width="2" fill="none" opacity=".8"/>
        <path d="M0 300 C80 270 160 290 290 330 V410 H0 Z" fill="#e6eef7"/>
      </svg>
      <div class="cover-back__photo" role="img" aria-label="Photo of two smiling office professionals"></div>
      <div class="contact">
        <div class="contact__title">vantor crew staffing</div>
        <div class="contact__row">
          <svg viewBox="0 0 10 10"><path d="M2 1 L4 1 L5 3 L4 4 C4.5 5.5 5 6 6 6.5 L7 5.5 L9 6.5 V8.5 C9 9 8.5 9.3 8 9.2 C4.5 8.7 1.3 5.5 0.8 2 C0.7 1.5 1.2 1 2 1 Z" fill="#1565b0"/></svg>
          <span>+00 123 456 7890</span>
        </div>
        <div class="contact__row">
          <svg viewBox="0 0 10 10"><rect x="0.5" y="2" width="9" height="6" fill="none" stroke="#1565b0"/><path d="M0.5 2 L5 5.5 L9.5 2" fill="none" stroke="#1565b0"/></svg>
          <span>hello@vantorcrew.example</span>
        </div>
        <div class="contact__row">
          <svg viewBox="0 0 10 10"><circle cx="5" cy="5" r="4.3" fill="none" stroke="#1565b0"/><path d="M0.7 5 H9.3 M5 0.7 C2.5 3 2.5 7 5 9.3 M5 0.7 C7.5 3 7.5 7 5 9.3" fill="none" stroke="#1565b0" stroke-width=".8"/></svg>
          <span>www.vantorcrew.example</span>
        </div>
      </div>
    </article>

    <article class="page cover-front">
      <div class="brand">
        <span class="brand__mark"></span>
        <span class="brand__name">vantor crew staffing</span>
      </div>
      <div class="cover-front__photo" role="img" aria-label="Photo of an engineer in a hard hat at an industrial site"></div>
      <svg class="wave" viewBox="0 0 290 410" preserveAspectRatio="none" aria-hidden="true">
        <defs>
          <linearGradient id="frontWave" x1="0" y1="0" x2="1" y2="1">
            <stop offset="0" stop-color="#3d9ad8"/>
            <stop offset=".55" stop-color="#1565b0"/>
            <stop offset="1" stop-color="#0b3d78"/>
          </linearGradient>
        </defs>
        <path d="M0 250 C90 215 200 205 290 225 V410 H0 Z" fill="url(#frontWave)"/>
        <path d="M0 262 C90 228 200 220 290 240" stroke="#fff" stroke-width="2.5" fill="none"/>
        <path d="M0 330 C110 300 200 300 290 280 V410 H0 Z" fill="#0b3d78" opacity=".55"/>
      </svg>
    </article>
  </section>

  <!-- inside spread -->
  <section class="spread spread--inside">
    <article class="page inside-left">
      <div class="inside-left__bar"></div>
      <div class="inside-left__body">
        <h2 class="section-head"><span class="section-head__num">1</span>Why choose vantor crew staffing (VCS)</h2>
        <p class="copy">We are a specialist recruitment partner for the oil and gas sector, connecting skilled people with projects across the globe.</p>
        <p class="copy">Our consultants bring years of field experience and a deep network of engineers, technicians and managers ready to deploy.</p>
        <p class="copy">We listen closely, act quickly and deliver shortlists that match both technical needs and company culture.</p>
        <h3 class="sub-head">Key Values</h3>
        <ul class="value-list">
          <li>Integrity in every placement</li>
          <li>Speed without compromise</li>
          <li>Safety first on every site</li>
          <li>Long term client partnerships</li>
        </ul>
      </div>
      <div class="services-band">
        <span class="services-band__title">Our services</span>
        <p class="copy">From single hires to full project crews, we cover every stage of the hiring cycle with care.</p>
      </div>
    </article>

    <article class="page inside-right">
      <svg class="wave" viewBox="0 0 280 410" preserveAspectRatio="none" aria-hidden="true">
        <defs>
          <linearGradient id="rightWave" x1="0" y1="0" x2="1" y2="0">
            <stop offset="0" stop-color="#3d9ad8"/>
            <stop offset="1" stop-color="#0b3d78"/>
          </linearGradient>
        </defs>
        <path d="M0 360 C90 340 190 345 280 320 V410 H0 Z" fill="url(#rightWave)"/>
        <path d="M0 368 C90 348 190 352 280 330" stroke="#fff" stroke-width="1.5" fill="none"/>
      </svg>
      <div class="inside-right__body">
        <h2 class="inside-right__title">Our service include</h2>
        <div class="service">
          <h3 class="service__name">Retained Search</h3>
          <p class="copy">A dedicated search for senior and critical roles, led by a named consultant from brief to offer.</p>
        </div>
        <div class="service">
          <h3 class="service__name">Contingency Search</h3>
          <p class="copy">Fast access to prescreened candidates for urgent vacancies, with fees payable only on success.</p>
        </div>
        <div class="service">
          <h3 class="service__name">Advertised Search</h3>
          <p class="copy">Targeted campaigns across industry channels to attract active job seekers in key regions.</p>
        </div>
        <div class="service">
          <h3 class="service__name">Talent Assessment</h3>
          <p class="copy">Structured interviews and technical tests to confirm skills before a candidate reaches you.</p>
        </div>
      </div>
    </article>
  </section>

</body>
</html>
```